Poly Bag Packaging Motorcycle Cables - Veronzo Brand

Poly Bag Dimensions: 33cm(H) x 24cm(W)
We would like to design a genuine Poly Bag Packaging for motorcycle cables.
Veronzo, is one of the leading companies for manufacturing Motorcycles, located in Egypt. Our company is offering high-quality products, the best in the local market, with very competitive prices.
We have a limited time to get this project done, So we Highly appreciate receiving your designs ASAP.
Target Market(s)
Motorcycle Spare parts Buyers
Font styles to use
Colors
Designer to choose colors to be used in the design.
Look and feel
Each slider illustrates characteristics of the customer's brand and the style your logo design should communicate.

```html
<!DOCTYPE html>
<html lang="en">
<head>
<meta charset="utf-8">
<title>Veronzo Throttle Cable Poly Bag</title>
<link rel="stylesheet" href="https://fonts.googleapis.com/css2?family=Tinos:wght@700&display=swap">
<style>
  :root {
    --paper: #ffffff;
    --brand-red: #ed1c2a;
    --brand-blue: #0b54a5;
    --ink: #000000;
    --steel-light: #e6e6e8;
    --steel-mid: #9a9a9d;
    --steel-dark: #1b1a1c;
  }
  html, body {
    margin: 0;
    padding: 0;
    overflow: hidden;
    background: var(--paper);
  }
  .bag {
    position: relative;
    width: 1200px;
    height: 1200px;
    background: var(--paper);
    overflow: hidden;
    font-family: "Tinos", "Times New Roman", serif;
  }
  .pattern-field {
    position: absolute;
    left: 34px;
    top: 36px;
    width: 1138px;
    height: 1136px;
    background:
      linear-gradient(160deg, rgba(237,28,42,0.9) 0%, rgba(237,28,42,0) 55%),
      linear-gradient(340deg, rgba(11,84,165,0.9) 0%, rgba(11,84,165,0) 55%),
      #7d3c75;
  }
  .brand-dot {
    position: absolute;
    left: 306px;
    top: 80px;
    width: 600px;
    height: 600px;
    border-radius: 50%;
    background: radial-gradient(circle at 50% 45%, var(--steel-light) 0%, var(--steel-mid) 60%, #5e5e62 100%);
  }
  .brand-name {
    position: absolute;
    left: 0;
    right: 0;
    top: 712px;
    margin: 0;
    text-align: center;
    font-size: 132px;
    font-weight: 700;
    line-height: 1;
    letter-spacing: 6px;
    color: var(--steel-light);
    text-transform: uppercase;
  }
  .product-label {
    position: absolute;
    left: 239px;
    top: 920px;
    width: 729px;
    height: 219px;
    background: var(--paper);
    border-radius: 24px;
    color: var(--ink);
    font-weight: 700;
  }
  .product-title {
    position: absolute;
    left: 0;
    right: 0;
    top: 22px;
    margin: 0;
    text-align: center;
    font-size: 68px;
    line-height: 1;
    letter-spacing: 1px;
  }
  .product-field {
    position: absolute;
    left: 168px;
    margin: 0;
    font-size: 42px;
    line-height: 1;
    white-space: nowrap;
  }
  .field-model { top: 98px; }
  .field-oem { top: 154px; }
</style>
</head>
<body>
  <main class="bag">
    <div class="pattern-field" role="img" aria-label="Diagonal red and blue stripe pattern background"></div>

    <div class="brand-dot"></div>
    <h1 class="brand-name">Veronzo</h1>

    <section class="product-label">
      <h2 class="product-title">THROTTLE CABLE</h2>
      <p class="product-field field-model">Model: .......................</p>
      <p class="product-field field-oem">OEM: .........................</p>
    </section>
  </main>
</body>
</html>
```